KBMR new business card design

We need a business card design for our established business which is Australia wide however based in Melbourne. We are a young team of Financial Planners who specialize in Insurance and Basic super advice for people like us.

We are people who help our clients get things done in a timely and cost effective manner whilst having a good time and a laugh along the way.

We would like this to have a consistent feel with our new e-brochure which i have attached from a color and font perspective.

Industry/Entity Type

Business

Requirements
Must have
• We do not need specific address details rather just the states we are in:

VIC/NSW/QLD/TAS
Nice to have
• Curved edge to mate the brochure

```html
<!DOCTYPE html>
<html lang="en">
<head>
<meta charset="utf-8">
<title>KBMR Business Card Design</title>
<link rel="stylesheet" href="https://fonts.googleapis.com/css2?family=Arimo:wght@400;700&family=Roboto+Condensed:wght@400;700&display=swap">
<style>
  :root {
    --page-bg: #e6e7e8;
    --green: #6cc04a;
    --green-light: #8fd46c;
    --green-dark: #3fa34d;
    --charcoal: #2b2a2a;
    --charcoal-light: #3d3c3c;
    --ink: #1d1d1d;
    --white: #ffffff;
    --muted: #dcdcdc;
  }
  * { box-sizing: border-box; margin: 0; padding: 0; }
  html, body { width: 1200px; height: 861px; overflow: hidden; }
  body {
    background: var(--page-bg);
    font-family: "Arimo", Arial, sans-serif;
    display: flex;
    align-items: center;
    justify-content: center;
    gap: 48px;
  }
  .card {
    position: relative;
    width: 530px;
    height: 330px;
    border-radius: 18px;
    overflow: hidden;
    background: var(--white);
    box-shadow: 0 10px 30px rgba(0,0,0,0.18);
  }
  .card--front .card__panel { background: linear-gradient(135deg, var(--green-dark) 0%, var(--green) 45%, var(--green-light) 100%); }
  .card--back .card__panel { background: linear-gradient(135deg, var(--charcoal) 0%, var(--charcoal-light) 60%, var(--charcoal) 100%); }
  .card__panel {
    position: absolute;
    inset: 0 140px 0 0;
    padding: 30px 0 0 24px;
  }
  .card__brand-zone {
    position: absolute;
    top: 0; right: 0; bottom: 0;
    width: 150px;
    background: var(--white);
    border-bottom-left-radius: 46px;
    border-left: 12px solid var(--ink);
    display: flex;
    align-items: center;
    justify-content: center;
  }
  .card--back .card__brand-zone { border-left-color: var(--green); }
  .brand { display: flex; align-items: center; gap: 8px; }
  .brand__square { width: 16px; height: 16px; background: var(--green); }
  .brand__name { font-weight: 700; font-size: 30px; color: var(--green-dark); letter-spacing: 1px; }

  .person__name { font-weight: 700; font-size: 31px; letter-spacing: 0.3px; line-height: 1; white-space: nowrap; }
  .card--front .person__name { color: var(--ink); }
  .card--back .person__name { color: var(--green); }
  .person__creds { font-weight: 400; font-size: 13px; margin-left: 6px; letter-spacing: 0; color: var(--white); }
  .person__role { color: var(--white); font-weight: 700; font-size: 20px; margin-top: 8px; }

  .entity { margin-top: 12px; color: var(--white); font-size: 14px; line-height: 1.3; }

  .contacts {
    margin-top: 24px;
    display: grid;
    grid-template-columns: 190px 160px;
    row-gap: 10px;
    color: var(--white);
    font-size: 15px;
  }
  .contact { display: flex; align-items: center; gap: 8px; white-space: nowrap; }
  .contact__icon {
    width: 24px; height: 24px;
    border: 2px solid var(--green);
    display: flex; align-items: center; justify-content: center;
  }
  .contact__icon svg { width: 16px; height: 16px; fill: var(--white); }

  .offices {
    position: absolute;
    left: 24px; bottom: 26px;
    font-family: "Roboto Condensed", "Arial Narrow", sans-serif;
    font-size: 12.5px;
    line-height: 1.75;
    list-style: none;
  }
  .office__state { font-weight: 700; }
  .card--front .office__state { color: var(--ink); }
  .card--back .office__state { color: var(--green); }
</style>
</head>
<body>

<article class="card card--front">
  <div class="card__panel">
    <h1 class="person__name">Daniel Hartley<span class="person__creds">ADFS, BBus, LRS</span></h1>
    <p class="person__role">Financial Adviser</p>
    <p class="entity">
      Kestrel Bay Money Rooms Pty Ltd<br>
      Authorised Representatives<br>
      Summitline Advisory Group Limited<br>
      Australian Financial Services Licensee
    </p>
    <ul class="offices">
      <li class="office__state">VICTORIA</li>
      <li class="office__state">NEW SOUTH WALES</li>
      <li class="office__state">QUEENSLAND</li>
      <li class="office__state">TASMANIA</li>
    </ul>
  </div>
  <div class="card__brand-zone">
    <div class="brand"><span class="brand__square"></span><span class="brand__name">KBMR</span></div>
  </div>
</article>

<article class="card card--back">
  <div class="card__panel">
    <h2 class="person__name">Daniel Hartley<span class="person__creds">ADFS, BBus, LRS</span></h2>
    <p class="person__role">Financial Adviser</p>
    <div class="contacts">
      <div class="contact">
        <span class="contact__icon"><svg viewBox="0 0 16 16"><path d="M3 1h3l1 4-2 1.2a9 9 0 0 0 4.8 4.8L11 9l4 1v3a2 2 0 0 1-2 2C6.5 15 1 9.5 1 3a2 2 0 0 1 2-2z"/></svg></span>
        1300 555 014
      </div>
      <div class="contact">
        <span class="contact__icon"><svg viewBox="0 0 16 16"><path d="M4 1h8v4H4zM1 6h14v7h-3v2H4v-2H1zM5 10v4h6v-4z"/></svg></span>
        03 9555 0182
      </div>
      <div class="contact">
        <span class="contact__icon"><svg viewBox="0 0 16 16"><path d="M1 3h14v10H1zM2.5 4.5v.3L8 9l5.5-4.2v-.3zM2.5 6.6v5h11v-5L8 10.8z"/></svg></span>
        daniel@kbmr.com.au
      </div>
      <div class="contact">
        <span class="contact__icon"><svg viewBox="0 0 16 16"><text x="8" y="12.5" text-anchor="middle" font-family="Arimo, Arial, sans-serif" font-weight="700" font-size="13" fill="#fff">@</text></svg></span>
        www.kbmr.com.au
      </div>
    </div>
    <ul class="offices">
      <li class="office__state">VICTORIA</li>
      <li class="office__state">NEW SOUTH WALES</li>
      <li class="office__state">QUEENSLAND</li>
      <li class="office__state">TASMANIA</li>
    </ul>
  </div>
  <div class="card__brand-zone">
    <div class="brand"><span class="brand__square"></span><span class="brand__name">KBMR</span></div>
  </div>
</article>

</body>
</html>
```